Lunar Ledger - Minimalistic Single Page Web Design

Project: We are in the process of creating a new Corp Identity. Design a website for our company incorporating the Logo recently designed and selected from a SketchHive contest. (attached)

Designers: For this project, you need to design a minimalistic single page, modern website. Beside text and image placement, you will also need to describe user interface, how content is presented and so on.
- Design Layout
- Design Image placements (if any)
- Design menu and buttons
- Design menu and buttons placements
- Design content layout
- Design overall effect and feel of website
- Design color scheme
- Design content style (tone and style of content, words type, how much)
- Design user interface (how do you scroll, what happens when you mouseover buttons, where do certain links and buttons lead you)

Coding Requirements: You need to design the website with a modern perspective on website visuals and effects. Jquery, HTML5 (no FLASH please). You do not need to code for this particular contest, but if you can also code, great, tell me and let me know how I can hire you to complete it. If you know someone that can code your vision, great, let me know. If not, you need to be clear and concise, and be willing to help me communicate with a developer to get the site executed. The web site needs to be modern and dynamic.

Company Name:
Lunar Ledger; Lunar-Ledger; LunarLedger

Domain: www.lunar-ledger.example

Company Industry:
Lunar Ledger provides consulting in areas of finance, accounting, business organization, and set up.
- Bookkeeping
- Project Management
- Budget Management
- Cash Management
- Receipt Management
- Filing and Records Management
- Training of administration and accounting staff
- Financial Reports
- Spreadsheets
- Graphs, charts and trend analysis
- Business set up
- Tax filings
- Payroll and HR

Clients:
- Small to medium size businesses
- Proprietors
- Entrepreneurs
- Mom & Pops Shops
- We cater to every industry

Corporate Identity:
- Past: I have never complete a webpage for my company. I did scratch several projects that were started and never completed. I fell in love with stick figures, whimsical designs, similar to that of "Cratebin", I believed in simplicity and minimalism. However, I was not effective in find the right people to complete my project. Bits and pieces of the website was designed, but never executed.

- Current: I need a webpage design. The web design must align with the current logo aesthetics.The current logo is new. I selected this logo for its simplicity and modern feel. It also incorporated an image of a trending graph, which fits with my company's profile. Still, I am leaning towards simple design, minimalism with boldness. I like my new webpage to be mature and professional, but I want it to portray energy and youth. So no "traditional corp" like design. I like new HTML5 elements, jquery and fun and beautiful forms and buttons. Less image is more.

Note: Please improvise according to your taste and professional perspective, you do not have to follow my suggestions word for word.

Features & Layout:
- Single page layout
- Vertical scroll
- Framed sections so that it looks good on the screen
- Well designed and strategically placed menu bar
- Fills a modern browser
- Beautiful color scheme that pops
- Incorporate Logo aesthetics

Fonts and Type:
- This is an element of the overall design
- I love clean fonts
- Fonts that adds meaning to the overall effect
- Clean

Sounds
- Please no cheesy sounds and background music

Images:
- To your liking
- But please, no lame corp people in suits
- No lame photographs
- I like stick figures
- I like whimsical illustrations

Landing Page:
- This should be the bulk of your design
- The landing page must be impressive, eye catchy
- Bold

Menu Bar:
- Header (introduction and landing page)
- Service & Products
- Company (about us)
- Affiliates and Clients (reference area)
- Contact (contact us area)
- Footer

Colors:
- Up to you, I just like things clean and easy to read
- No black background behind text
- Incorporate Logo Colors

Web Effects:
- According to your liking
- You will need to be involve to communicate the layout and design to the developer, so you need to be clear in your design.

Content:
- You personally don't have to come up with the content, but if you can great.
- I will help come up with the content throughout the contect timeframe, just let me know what you want
- I do not like too much content in my website. The most for each section is 2-3 lines if any.
- Combination could also be one liners.
- I like minimalistic approach.
- If you are not creating the final content, you need to show what type of content need to be created and in what style or tone.

Samples and Inspirations:
- http://scrollkin.example/
- http://zentrovo.example/#top
- http://brightmopservices.example/#about
- http://pixelgazette.example/inspiration/23-inspiring-single-page-designs
- http://www.tobiaskernstudio.example/
- http://www.ravelquist.example/

This I do not want:
- Too much popups (none if possible)
- Images of people
- Images of people in suits
- Stereotypical images of accountants
- Scrolling marquee
- Clip arts
Updates

Designers, I want to stress the fact that I am looking for a design, not simply a website. The website is 1 page long. Text and content should be minimal. So this means that the design has to do most of the talking. Please do not submit template like web designs, I can pull this off myself if needed. I need you to design a great header, footer and the connecting tissue from landing to end of the page. The entire design needs to flow.

Again, please do not use images of corp people or anything like that. Please think outside the box in how you want to express the company.

Some ideas:
An illustration from beginning to end of the website, have a story.
Add colors to the back ground. 
The background should not get in the way of reading the text, but it does not have to be boring.
Be bold in your design.

Also, please describe more about your design when you submit. Please don't submit a template like design and have no explanation for your actions.

Also, fee free to ask me questions. I am here to help. I check this everyday, so please contact if you need anything.

Designers, please read the details of my post before you submit the design.

If you have a great concept idea but is worry, you can go ahead and submit a pencil draft and ask my opinion before you work anymore on it.

Please see the website samples below for what I am really looking for:

Reason: Hi everyone, I am extending the deadline. It looks like some design are still pending completion, and I want you to have enough time to work on it.

Industry/Entity Type

Accounting

```html
<!DOCTYPE html>
<html lang="en">
<head>
<meta charset="utf-8">
<title>Lunar Ledger</title>
<link rel="stylesheet" href="https://fonts.googleapis.com/css2?family=Lato:wght@400;700&family=Quicksand:wght@500&family=Noto+Sans:ital,wght@0,400;0,700;1,400&display=swap">
<style>
  :root {
    --brand-blue: #141e9c;
    --white: #ffffff;
    --sky-light: #d9d9d9;
    --land-mid: #8a8a8a;
    --asphalt: #2b2b2b;
    --asphalt-deep: #1a1a1a;
    --avatar-fill: #d4d4d4;
    --avatar-ring: #cfcfcf;
  }
  * { box-sizing: border-box; margin: 0; padding: 0; }
  html, body { width: 1200px; height: 1097px; overflow: hidden; }
  body { position: relative; background: var(--white); font-family: "Noto Sans", sans-serif; }

  .hero-photo {
    position: absolute; left: 0; top: 0; width: 1200px; height: 198px;
    background: linear-gradient(180deg, var(--sky-light) 0%, #bdbdbd 42%, var(--land-mid) 60%, #4a4a4a 100%);
  }
  .brand {
    position: absolute; left: 400px; top: 46px; width: 400px; height: 84px;
    background: var(--white);
    display: flex; align-items: center; justify-content: center;
  }
  .brand-name {
    font-family: "Quicksand", sans-serif; font-weight: 500;
    font-size: 44px; color: var(--brand-blue); letter-spacing: 0.5px;
  }

  .tagline {
    position: absolute; left: 0; top: 198px; width: 1200px; height: 132px;
    background: var(--white);
    text-align: center; color: var(--brand-blue);
    font-family: "Lato", sans-serif; font-weight: 400;
    font-size: 31px; line-height: 36px; padding-top: 30px;
  }
  .tagline strong { font-weight: 700; }

  .road-photo {
    position: absolute; left: 0; top: 330px; width: 1200px; height: 170px;
    background: linear-gradient(180deg, var(--asphalt-deep) 0%, var(--asphalt) 55%, #3a3a3a 100%);
  }

  .social {
    position: absolute; top: 318px; left: 549px;
    display: flex; gap: 2px; list-style: none;
  }
  .social li { width: 24px; height: 24px; background: var(--brand-blue); }

  .main-nav {
    position: absolute; top: 384px; left: 344px;
    display: flex; gap: 3px; list-style: none;
  }
  .main-nav a {
    display: flex; align-items: center; justify-content: center;
    width: 100px; height: 38px; background: var(--white);
    color: var(--brand-blue); text-decoration: none;
    font-family: Arial, Helvetica, sans-serif; font-size: 14.5px;
  }
  .main-nav li:nth-child(2) a, .main-nav li:nth-child(5) a { width: 101px; }

  .content {
    position: absolute; left: 0; top: 500px; width: 1200px; height: 597px;
    background: var(--brand-blue); color: var(--white);
  }
  .section-title {
    position: absolute; left: 125px;
    font-family: "Noto Sans", sans-serif; font-weight: 400; font-size: 23px;
  }
  .about-title { top: 54px; }
  .title-rule {
    position: absolute; left: 244px; top: 64px; width: 836px; height: 13px;
    background-image: radial-gradient(circle, rgba(255,255,255,0.85) 0.8px, transparent 1px);
    background-size: 3px 3px;
  }
  .about-text {
    position: absolute; left: 125px; top: 103px; width: 955px;
    font-size: 12.6px; line-height: 24px; text-align: justify;
  }
  .team-title { top: 214px; }

  .team {
    position: absolute; left: 0; top: 281px; width: 1200px; list-style: none;
  }
  .member { position: absolute; width: 220px; text-align: center; }
  .member:nth-child(1) { left: 119px; }
  .member:nth-child(2) { left: 370px; }
  .member:nth-child(3) { left: 622px; }
  .member:nth-child(4) { left: 873px; }
  .avatar {
    display: block; margin: 0 auto; width: 192px; height: 192px; border-radius: 50%;
    background: var(--white); padding: 8px;
  }
  .avatar span {
    display: block; width: 100%; height: 100%; border-radius: 50%;
    background: var(--avatar-fill); border: 1px solid var(--avatar-ring);
  }
  .member-name { margin-top: 18px; font-weight: 700; font-size: 19px; line-height: 24px; }
  .member-role { font-style: italic; font-size: 14.5px; line-height: 24px; }
</style>
</head>
<body>
  <header>
    <div class="hero-photo" role="img" aria-label="Black and white photograph of an open desert highway stretching towards distant mountains"></div>
    <div class="brand"><span class="brand-name">lunar ledger</span></div>
    <h1 class="tagline">WE WILL <strong>GUIDE</strong> YOU<br>TO THE RIGHT <strong>PATH</strong></h1>
    <div class="road-photo" role="img" aria-label="Close-up black and white photograph of asphalt road with white lane markings"></div>
    <ul class="social" aria-label="Social links">
      <li></li><li></li><li></li><li></li>
    </ul>
    <nav>
      <ul class="main-nav">
        <li><a href="#home">HOME</a></li>
        <li><a href="#company">COMPANY</a></li>
        <li><a href="#services">SERVICES</a></li>
        <li><a href="#clients">CLIENTS</a></li>
        <li><a href="#contact">CONTACT</a></li>
      </ul>
    </nav>
  </header>

  <main class="content" id="company">
    <h2 class="section-title about-title">About Us</h2>
    <div class="title-rule"></div>
    <p class="about-text">Lorem ipsum dolor sit amet, consectetur adipiscing elit. Integer ac neque ligula. Pellentesque bibendum, lorem sit amet pretium ultricies, odio purus faucibus eros, a scelerisque orci leo ac libero. Sed fringilla ultricies rutrum. Praesent lacus magna, pharetra eu convallis at, consectetur vitae libero. Praesent vel turpis sem. Donec feugiat ultrices molestie.</p>

    <h2 class="section-title team-title">Meet our Team</h2>
    <ul class="team">
      <li class="member">
        <span class="avatar" role="img" aria-label="Team member portrait placeholder"><span></span></span>
        <p class="member-name">Robert Doe</p>
        <p class="member-role">Designation</p>
      </li>
      <li class="member">
        <span class="avatar" role="img" aria-label="Team member portrait placeholder"><span></span></span>
        <p class="member-name">Robert Doe</p>
        <p class="member-role">Designation</p>
      </li>
      <li class="member">
        <span class="avatar" role="img" aria-label="Team member portrait placeholder"><span></span></span>
        <p class="member-name">Robert Doe</p>
        <p class="member-role">Designation</p>
      </li>
      <li class="member">
        <span class="avatar" role="img" aria-label="Team member portrait placeholder"><span></span></span>
        <p class="member-name">Robert Doe</p>
        <p class="member-role">Designation</p>
      </li>
    </ul>
  </main>
</body>
</html>
```